Litigation services brochure for TRV.law

improve aesthetics and sync with website color scheme and new staff to emphasize law firm's litigation capabilities. Describe Litigation director, senior attorneys, attorneys, and general capabilities of the firm, licenses to practice, representative trasnactions and litigation experience. Take profile info from individual attorneys listed in the .doc and correlate with www.trv.law profiles for same attorneys. Update photos as needed. I'm not sure what other words I need to add, but this thing says there needs to be more words in my project description. read the brochure attached, and it should be pretty self explanatory. We have lots of info and content on there, we just want it to look better and reflect the updated color scheme of the site (a few of the color bar colors have changed order and color).

Target Market(s)

Houston, Denver

Font styles to use
Serif

Requirements
Must have
• Color scheme that matches www.trv.law
Nice to have
• Better aesthetics and content optimization

```html
<!DOCTYPE html>
<html lang="en">
<head>
<meta charset="utf-8">
<title>TRV.law Litigation Brochure</title>
<link href="https://fonts.googleapis.com/css2?family=Tinos:ital,wght@0,400;0,700;1,400;1,700&family=PT+Sans+Narrow:wght@400;700&display=swap" rel="stylesheet">
<style>
:root{
  --stage:#0b0b0b;
  --panel:#3a393b;
  --panel-dark:#323133;
  --ink:#f2f2f2;
  --muted:#d8d8d8;
  --yellow:#f2c21b;
  --green:#5f9a3c;
  --darkgreen:#264a2a;
  --orange:#f08a2a;
  --tan:#d6ad6b;
  --blue:#2a6fb3;
  --navy:#1f4f7f;
  --red:#b3262e;
}
*{margin:0;padding:0;box-sizing:border-box}
html,body{width:1200px;height:1200px;overflow:hidden;background:var(--stage)}
body{position:relative;font-family:"PT Sans Narrow",sans-serif;color:var(--muted)}
.spread{position:absolute;background:var(--panel);overflow:hidden}
.spread--cover{left:82px;top:71px;width:750px;height:485px}
.spread--inside{left:300px;top:627px;width:755px;height:489px;box-shadow:0 22px 30px rgba(0,0,0,.6)}
.photo{position:absolute}
.photo--books{left:0;top:0;width:374px;height:485px;background:linear-gradient(90deg,#2c2b2d 0%,#4a494b 30%,#3c3b3d 55%,#515052 75%,#3a393b 100%)}
.photo--handshake{left:374px;top:118px;width:376px;height:172px;background:linear-gradient(120deg,#4c4b4d 0%,#8d8c8e 45%,#b5b4b6 70%,#6a696b 100%)}
.fold{position:absolute;top:0;width:26px;height:100%;background:linear-gradient(90deg,rgba(0,0,0,.35),rgba(0,0,0,0))}
.colorbar{position:absolute;display:flex;height:2px}
.colorbar span{flex:1}
.office{position:absolute;left:44px;font-size:7.2px;line-height:8.6px;color:var(--ink)}
.office__label{display:block;width:74px;height:7px;font-size:7px;line-height:7px;color:#222;padding-left:2px;margin-bottom:10px;text-transform:uppercase}
.monogram{position:absolute;left:274px;top:370px;display:flex;align-items:center;gap:4px;font-family:"Tinos",serif;font-size:22px;color:#8b8a8c}
.monogram i{display:block;width:7px;height:7px;background:#8b8a8c}
.firm{position:absolute;left:374px;width:376px;top:362px;text-align:center;font-family:"Tinos",serif;color:var(--ink);font-variant:small-caps}
.firm__name{font-size:21px;letter-spacing:.3px}
.firm__tag{font-size:13px;margin-top:4px}
.photo--signing{left:0;top:0;width:755px;height:230px;background:linear-gradient(100deg,#3f3e40 0%,#6c6b6d 35%,#8f8e90 55%,#a7a6a8 80%,#77767a 100%)}
.shade{position:absolute;left:0;top:0;width:378px;height:230px;background:rgba(40,40,42,.35)}
.headline{position:absolute;left:64px;top:60px;font-family:"Tinos",serif;font-weight:700;font-size:21px;line-height:25px;color:#fff}
.pitch{position:absolute;left:438px;top:64px;width:290px;font-family:"Tinos",serif;font-style:italic;font-size:10.4px;line-height:12px;color:#fff}
.pitch b{display:block;margin-top:12px;font-size:10.8px}
.tabs{position:absolute;left:0;top:230px;width:378px;height:20px;display:flex}
.tab{flex:1;padding:2px 0 0 21px;font-size:7px;line-height:8px;font-weight:700;color:#fff}
.tab--orange{background:var(--orange)}
.tab--green{background:var(--green);padding-left:15px}
.tab--tan{background:var(--tan);color:#3a2e1c;padding-left:14px}
.tab--blue{background:var(--navy);padding-left:9px}
.practice{position:absolute;top:277px;width:78px;font-size:6.6px;line-height:9.6px;color:var(--muted)}
.summary{position:absolute;left:34px;top:378px;width:310px;font-size:6.6px;line-height:9.8px;text-align:justify;color:var(--muted)}
.summary b{color:#fff}
.rightpage{position:absolute;left:378px;top:230px;width:377px;height:259px;background:var(--panel-dark)}
.col{position:absolute;top:46px;font-size:6.6px;line-height:8.6px;color:var(--muted)}
.col h3{font-size:6.6px;font-weight:700;text-transform:uppercase;margin-bottom:8px}
.col p{margin-bottom:8px}
.c-orange{color:var(--orange)}.c-green{color:var(--green)}.c-tan{color:var(--tan)}.c-blue{color:var(--blue)}
.states{font-weight:700;color:#fff;margin-bottom:8px;white-space:nowrap}
.states div{display:flex;justify-content:space-between;gap:4px}
</style>
</head>
<body>

<section class="spread spread--cover">
  <div class="photo photo--books" role="img" aria-label="Close-up photo of leather-bound law books on a shelf"></div>
  <div class="photo photo--handshake" role="img" aria-label="Black and white photo of two people in suits shaking hands"></div>
  <div class="fold" style="left:374px"></div>
  <div class="colorbar" style="left:4px;top:118px;width:370px">
    <span style="background:var(--yellow)"></span><span style="background:var(--darkgreen)"></span><span style="background:var(--yellow)"></span><span style="background:var(--red)"></span>
  </div>
  <div class="colorbar" style="left:374px;top:118px;width:376px">
    <span style="background:var(--yellow)"></span><span style="background:var(--navy)"></span><span style="background:var(--yellow)"></span><span style="background:var(--orange)"></span><span style="background:var(--red)"></span>
  </div>

  <div class="office" style="top:340px">
    <span class="office__label" style="background:var(--yellow)">Denver</span>
    1480 Larimer Street, Suite 2210, Denver, Colorado 80202<br>Office: (720) 555-0142<br>Fax: (720) 555-0143
  </div>
  <div class="office" style="top:404px">
    <span class="office__label" style="background:var(--orange)">Houston</span>
    275 Fannin Street, Suite 318, Houston, Texas 77002<br>Office: (713) 555-0186<br>Fax: (713) 555-0187
  </div>
  <div class="monogram"><i></i>TRV</div>

  <div class="firm">
    <div class="firm__name">Thornton Reyes &amp; Vale</div>
    <div class="firm__tag">Attorneys at Law</div>
  </div>
</section>

<section class="spread spread--inside">
  <div class="photo photo--signing" role="img" aria-label="Black and white photo of hands signing documents at a desk"></div>
  <div class="shade"></div>
  <div class="fold" style="left:378px;height:230px"></div>

  <h1 class="headline">ENERGY.<br>INTELLECTUAL.<br>CORPORATE.<br>ESTATES.<br>LITIGATION.</h1>
  <p class="pitch">Our firm can represent the entirety of your individual or business' vertical integration in the market. From oil &amp; gas title research to biotech patents, software copyright and trade secret protection, commercial property contract negotiations, licensing and deal drafting, dispute resolution, and complex litigation…<b>We want to be your only firm.</b></p>

  <div class="tabs">
    <div class="tab tab--orange">Oil, Gas &amp;<br>Other Minerals</div>
    <div class="tab tab--green">Intellectual<br>Property</div>
    <div class="tab tab--tan">Residential &amp;<br>Commercial</div>
    <div class="tab tab--blue">Entity and Estate<br>Management</div>
  </div>

  <p class="practice" style="left:21px">Our firm has the team and experience ready to help develop and manage your oil and gas interests, from inception through production, operation, diligence, acquisitions, and divestitures.</p>
  <p class="practice" style="left:110px">We're ready to assist in identifying, protecting, managing, and enforcing intellectual property rights in your business, including patents, trademarks, copyrights, and trade secrets</p>
  <p class="practice" style="left:202px">We have the knowledge and staff necessary to assist with your real and commercial property project development, including diligence, transactions, landlord &amp; tenant negotiations, and closings</p>
  <p class="practice" style="left:292px">TRV is ready to help you maintain, modify, or create an entity or estate plan that works, helping to minimize tax exposure, short and long term, and maintain control over your assets.</p>

  <p class="summary">If you create, own, manage, or direct any type of business, <b>you have issues related to our core practice areas.</b> We are ready to handle the entire vertical stack of your company, estate, or property issues. Not merely an energy, IP, or title firm, TRV is structured to handle your intellectual property issues, business operations and transactions, contract drafting and negotiations, acquisition and merger diligence and negotiations, as well as dispute resolution and litigation related to these interests. We want to assist in expanding your business, protecting your ideas, developing and maintaining your rights in property assets, acquiring new businesses and properties, managing your employees, and identifying and protecting against liabilities, infringers, and tortfeasors. With offices in the energy and technology hubs of Houston, TX, and Denver, CO, as well as licenses to practice in many other states across the country, we're ready.</p>

  <div class="rightpage">
    <div class="col" style="left:16px;width:88px">
      <h3 class="c-orange">Our Clients</h3>
      <p>TRV attorneys represent clients in various fields, worldwide:</p>
      <p><span class="c-orange">Oil &amp; Gas Operators</span><br>Producers / Manufacturers<br>Design / Engineering Firms<br>Inventors / Artists / Developers<br>Business Owners and Partners<br>Estates Admins and Trustees<br>Startups to Large Businesses<br>Partnerships and Corporations</p>
    </div>
    <div class="col" style="left:110px;width:92px">
      <h3 class="c-green">Our Attorneys</h3>
      <p>We have licenses, certifications, and experience necessary to assist regionally, nationally, and globally.</p>
      <p class="c-green">Currently, TRV has licenses to practice in:</p>
      <div class="states">
        <div><span>Texas</span><span>Oregon Pennsylvania</span></div>
        <div><span>Colorado</span><span>Wyoming</span></div>
        <div><span>Florida</span><span>Utah USPTO</span></div>
        <div><span>New Mexico</span><span>5th Cir.</span></div>
        <div><span>N. Dakota Oklahoma</span><span>US Sup Ct.</span></div>
      </div>
      <p class="c-blue">See our attorneys here</p>
    </div>
    <div class="col" style="left:214px;width:76px">
      <h3 class="c-tan">Our Staff</h3>
      <p>TRV was founded on principles of transparency and fairness. We want our employees to love working for us so that they will love working for you.</p>
      <p><span class="c-tan">Our rates are typically lower than our competitors, while our staff is paid more.</span><br>This means clients get consistent, reliable performance and work product.<br>Not excuses.</p>
    </div>
    <div class="col" style="left:299px;width:72px">
      <h3 class="c-blue">Our Offices</h3>
      <p>We have offices located in Houston and Denver, with attorneys ready to work with you.</p>
      <p><span class="c-blue">Houston<br>Bayou Commerce Plaza</span><br>275 Fannin, Suite 318<br>Houston, TX 77002</p>
      <p><span class="c-blue">Denver<br>Front Range Tower</span><br>1480 Larimer,<br>Suite 2210<br>Denver, CO 80202</p>
    </div>
    <div class="colorbar" style="left:0;top:223px;width:377px">
      <span style="background:var(--orange)"></span><span style="background:var(--green)"></span><span style="background:var(--tan)"></span><span style="background:var(--navy)"></span>
    </div>
  </div>
</section>

</body>
</html>
```